Copper Lantern Vapors - Premium labels

Copper Lantern Vapors is a business that has multiple retail locations where we sell e-cigs and liquid for e-cigs. We have our own house line of liquid but we're looking for expand our business with a premium brand of liquid. This label would be for our premium liquid bottles. We'd like to go with a Four Horseman of the Apocalypse theme. So I'm thinking we would have 4 flavors named White, Black, Red, and Pale.

Example label template attached.

Please let me know if you have any questions!

Thanks
(attaching our standard logo as reference)

Industry/Entity Type

Business

Requirements
Must have
• The branding should be for the Four Horseman theme. We want this to seem like it's own brand. Should have four different variations of labels - one each for White, Black, Red, and Pale. They can be very similar (or different), no preference at the moment.

```html
<!DOCTYPE html>
<html lang="en">
<head>
<meta charset="utf-8">
<title>Copper Lantern Vapors – Red Label</title>
<link href="https://fonts.googleapis.com/css2?family=Montserrat:wght@700&family=Black+Ops+One&family=Roboto+Condensed:wght@400;700&family=Oswald:wght@300&display=swap" rel="stylesheet">
<style>
  :root{
    --ink:#000000;
    --blood:#c1161e;
    --blood-dark:#6e0d10;
    --title-red:#c51a22;
    --white:#ffffff;
    --cut-blue:#4d8fd6;
    --bleed-pink:#e0248a;
  }
  html,body{margin:0;padding:0;overflow:hidden;background:var(--ink);}
  .label{position:relative;width:1200px;height:1121px;background:var(--ink);overflow:hidden;
    font-family:"Roboto Condensed",Arial,sans-serif;color:var(--white);}
  .guides{position:absolute;inset:0;}
  .red-band{position:absolute;left:0;top:232px;width:1200px;height:640px;background:var(--blood);}
  .riders{position:absolute;left:250px;top:565px;width:740px;height:310px;
    background:linear-gradient(180deg,rgba(0,0,0,.55),rgba(0,0,0,.9));border-radius:6px;}
  .brand{position:absolute;left:275px;top:240px;display:flex;align-items:center;gap:20px;}
  .brand-mark{width:110px;height:110px;border-radius:50%;background:var(--white);flex:none;}
  .brand-name{font-family:"Montserrat",sans-serif;font-weight:700;color:var(--white);
    line-height:1.1;white-space:nowrap;}
  .brand-name .line1{display:block;font-size:50px;letter-spacing:1px;}
  .brand-name .line2{display:block;font-size:42px;letter-spacing:17px;margin-left:92px;}
  .flavor{position:absolute;left:0;width:1254px;top:444px;text-align:center;
    font-family:"Black Ops One",sans-serif;font-size:108px;color:var(--blood-dark);line-height:1;}
  .theme-title{position:absolute;left:0;width:1216px;top:884px;text-align:center;
    font-family:"Black Ops One",sans-serif;font-size:56px;line-height:62px;color:var(--title-red);}
  .fine-print{position:absolute;left:250px;top:105px;transform:rotate(90deg);
    transform-origin:top left;font-size:21px;line-height:26.5px;white-space:nowrap;}
  .fine-print b{font-weight:700;}
  .volume{position:absolute;left:242px;top:700px;transform:rotate(90deg);transform-origin:top left;
    font-weight:700;font-size:20px;line-height:24px;}
  .nicotine-warning{position:absolute;left:999px;top:660px;width:563px;height:107px;box-sizing:border-box;
    transform:rotate(-90deg);transform-origin:top left;border:3px solid var(--white);border-radius:22px;
    font-family:"Oswald",sans-serif;font-weight:300;font-size:35px;line-height:43px;
    padding:8px 0 0 16px;white-space:nowrap;overflow:hidden;}
  .icons{position:absolute;left:990px;top:670px;width:130px;height:270px;}
</style>
</head>
<body>
<div class="label">
  <div class="red-band"></div>

  <svg class="guides" width="1200" height="1121" viewBox="0 0 1200 1121" aria-hidden="true">
    <rect x="25" y="25" width="1150" height="1070" rx="60" fill="none" stroke="var(--cut-blue)" stroke-width="2" stroke-dasharray="22 12"/>
    <rect x="47" y="47" width="1106" height="1026" rx="45" fill="none" stroke="var(--bleed-pink)" stroke-width="2"/>
    <rect x="70" y="70" width="1060" height="980" rx="35" fill="none" stroke="var(--cut-blue)" stroke-width="2" stroke-dasharray="22 12"/>
  </svg>

  <div class="riders" role="img" aria-label="Silhouettes of the four horsemen riding across the red band"></div>

  <div class="brand">
    <div class="brand-mark"></div>
    <div class="brand-name"><span class="line1">COPPER LANTERN</span><span class="line2">VAPORS</span></div>
  </div>

  <div class="flavor">RED</div>

  <div class="theme-title">FOUR HORSEMAN<br>OF THE APOCALYPSE</div>

  <div class="fine-print">
    <b>Ingredients:</b> USP Grade Glycerin, USP Grade Propylene Glycol,<br>
    Natural &amp; Artificial Flavoring, USP Grade Nicotine &nbsp;<b>Prop 65</b><br>
    <b>Warning:</b> This product may contain a chemical known to the<br>
    state of California to cause birth defects, or other reproductive harm.<br>
    <b>NOT FOR UNDERAGE SALES</b><br>
    <b>KEEP AWAY FROM CHILDREN AND PETS</b>
  </div>

  <div class="volume">60ML<br>70/30</div>

  <div class="nicotine-warning">WARNING: This product contains nicotine<br>Nicotine is an addictive chemical.</div>

  <svg class="icons" viewBox="0 0 130 270" aria-hidden="true">
    <g fill="var(--white)">
      <rect x="35" y="2" width="84" height="50"/>
      <g fill="var(--ink)">
        <rect x="35" y="8" width="84" height="3"/><rect x="35" y="16" width="84" height="3"/>
        <rect x="35" y="24" width="84" height="3"/><rect x="35" y="32" width="84" height="3"/>
        <rect x="35" y="40" width="84" height="3"/>
        <rect x="35" y="2" width="30" height="22"/>
      </g>
      <circle cx="96" cy="102" r="24"/>
      <text x="96" y="111" text-anchor="middle" font-family="Roboto Condensed, sans-serif" font-weight="700" font-size="24" fill="var(--ink)">21+</text>
      <circle cx="96" cy="168" r="24"/>
      <path d="M78 230a18 18 0 0 1 32-8l4-5v16h-16l6-5a12 12 0 0 0-20 6z M114 238a18 18 0 0 1-32 8l-4 5v-16h16l-6 5a12 12 0 0 0 20-6z"/>
    </g>
    <g fill="none" stroke="var(--white)" stroke-width="4">
      <rect x="22" y="112" width="42" height="42" transform="rotate(45 43 133)"/>
      <rect x="22" y="184" width="42" height="42" transform="rotate(45 43 205)"/>
    </g>
    <g fill="var(--white)">
      <rect x="40" y="119" width="6" height="18"/><rect x="40" y="141" width="6" height="6"/>
      <circle cx="43" cy="205" r="8"/>
    </g>
  </svg>
</div>
</body>
</html>
```